Computer Consulting Brochure

Computer Consulting services for schools, small businesses, local governments and medical offices. We design networks, security, monitoring, applications for these environments.
Updates
Project Deadline Extended Reason: I provided a condensed document so as not to overwhelm designers. This document covers only pertinent info that can be further condensed if necessary for physical size constraints. Added Friday, April 7, 2017
Target Market(s)
Schools, Small Businesses, Medical Offices, Local Governments. 4 brochures that are identical except for a section that specifically describes the 4 markets.
Industry/Entity Type
Computer
Colors
Designer to choose colors to be used in the design.
Look and feel
Each slider illustrates characteristics of the customer's brand and the style your logo design should communicate.

```html
<!DOCTYPE html>
<html lang="en">
<head>
<meta charset="utf-8">
<title>Keystone Net – IT Services Brochure</title>
<link rel="stylesheet" href="https://fonts.googleapis.com/css2?family=Barlow+Condensed:wght@300;400;500;600;700&family=Barlow+Semi+Condensed:wght@400;500&display=swap">
<style>
  :root{
    --yellow:#f2b21e;
    --yellow-deep:#e09e10;
    --yellow-soft:#fbe7a6;
    --teal:#1f9bbb;
    --teal-deep:#1788a6;
    --teal-light:#6cc5d8;
    --ink:#2f3338;
    --grey:#8a8f94;
    --paper:#ffffff;
    --backdrop:#e9e6e1;
  }
  *{box-sizing:border-box;margin:0;padding:0}
  html,body{width:1200px;height:1200px;overflow:hidden;background:var(--backdrop)}
  body{position:relative;font-family:"Barlow Semi Condensed",Arial,sans-serif;color:var(--ink)}
  .spread{position:absolute;left:225px;width:750px;height:570px;display:flex;background:var(--paper);box-shadow:0 2px 10px rgba(0,0,0,.18)}
  .spread--outside{top:20px}
  .spread--inside{top:610px}
  .panel{position:relative;width:250px;height:570px;overflow:hidden}
  .heading{font-family:"Barlow Condensed",sans-serif;font-weight:600;color:var(--teal-deep);text-transform:uppercase;line-height:1}
  .lead{font-family:"Barlow Condensed",sans-serif;font-weight:600;color:var(--teal-deep);font-size:11px;line-height:1.2}
  .body{font-size:8.5px;line-height:1.38;color:var(--ink)}
  .body p{margin-bottom:6px}
  .bullets{list-style:none}
  .bullets li{position:relative;padding-left:9px;margin-bottom:5px;font-size:8.5px;line-height:1.35}
  .bullets li::before{content:"";position:absolute;left:0;top:2px;width:5px;height:5px;background:var(--teal-light)}

  /* outside: dealerships */
  .dealers{padding:14px 12px}
  .dealers .heading{font-size:19px;margin-bottom:4px}
  .dealers .lead{margin-bottom:9px}
  .dealers .bullets{margin-bottom:8px}
  .dealers .photo-fade{position:absolute;left:0;right:0;bottom:0;height:90px;background:linear-gradient(to bottom,rgba(255,255,255,0),#d9dde2 60%,#c7ccd3)}
  .dealers .body{position:relative}

  /* outside: projects + solutions */
  .projects-top{height:265px;padding:14px 10px 0 10px}
  .projects-top .heading{font-size:19px;margin-bottom:6px}
  .projects-top .bullets li{font-size:7.8px;margin-bottom:3px;line-height:1.22}
  .solutions{position:absolute;left:0;right:0;bottom:0;height:305px;background:linear-gradient(to bottom,var(--teal-light),var(--teal) 55%,var(--teal-deep));padding:24px 10px 0;color:#fff}
  .solutions-text{font-family:"Barlow Condensed",sans-serif;font-weight:500;font-size:14.8px;line-height:1.3;text-transform:uppercase;text-align:center;margin-bottom:16px}
  .contact{list-style:none;font-family:"Barlow Condensed",sans-serif;font-weight:500;font-size:10.5px;padding-left:12px}
  .contact li{display:flex;align-items:center;gap:8px;margin-bottom:4px}
  .contact svg{width:11px;height:11px;flex:none}

  /* outside: cover */
  .cover-photo{position:absolute;left:0;top:0;right:0;height:290px;background:linear-gradient(135deg,#eef2f5 0%,#c9d6df 45%,#7f95a6 100%)}
  .brand{position:absolute;top:12px;right:14px;font-family:"Barlow Condensed",sans-serif;font-weight:500;font-size:20px;color:var(--grey);display:flex;align-items:center;gap:5px}
  .brand-dot{width:7px;height:7px;border-radius:50%;background:var(--grey)}
  .cover-band{position:absolute;left:0;right:0;bottom:0;height:280px;background:linear-gradient(to bottom,#f5bf3a,var(--yellow) 50%,#eea81a);padding:14px 12px 0 12px;color:#fff}
  .cover-title{font-family:"Barlow Condensed",sans-serif;font-weight:300;font-size:46px;line-height:.9;text-transform:uppercase;padding-bottom:5px;border-bottom:2px solid #fff;margin-bottom:7px}
  .cover-sub{font-family:"Barlow Condensed",sans-serif;font-size:21px;line-height:1.05;color:var(--teal-deep);margin-bottom:8px}
  .cover-sub b{font-weight:700;text-transform:uppercase}
  .cover-sub span{font-weight:400}
  .cover-for{display:flex;gap:18px}
  .cover-for .for{font-family:"Barlow Condensed",sans-serif;font-weight:300;font-size:20px;line-height:1}
  .cover-item h3{font-family:"Barlow Condensed",sans-serif;font-weight:600;font-size:15px;color:var(--teal-deep);line-height:1;text-transform:uppercase;margin-bottom:3px}
  .cover-item p{font-size:8.8px;line-height:1.2;text-transform:uppercase;margin-bottom:8px}

  /* inside */
  .inside-band{position:absolute;top:0;left:0;right:0;height:72px}
  .band-teal{background:linear-gradient(to right,var(--teal-light),var(--teal))}
  .band-yellow{background:var(--yellow)}
  .why-title{position:absolute;left:20px;top:22px;font-family:"Barlow Condensed",sans-serif;font-weight:700;font-size:36px;color:#fff;text-transform:uppercase;line-height:1}
  .what-title{position:absolute;left:16px;top:14px;font-family:"Barlow Condensed",sans-serif;font-weight:600;font-size:17px;color:#fff;text-transform:uppercase;line-height:1.05}
  .inside-photo{position:absolute;left:0;top:330px;width:500px;height:240px;background:linear-gradient(100deg,#e8b79a 0%,#c98aa6 40%,#a876b8 70%,#e7a77f 100%)}
  .inside-photo::before{content:"";position:absolute;left:0;right:0;top:0;height:80px;background:linear-gradient(to bottom,#fff,rgba(255,255,255,0))}
  .why-col{position:absolute;top:90px;width:240px;padding:0 12px 0 20px}
  .why-col--a{left:0}
  .why-col--b{left:250px;padding-left:18px}
  .why-col .lead{margin-bottom:6px}
  .why-col .body{font-size:9.3px;line-height:1.4}
  .what-panel{background:linear-gradient(to bottom,#fffdf7,var(--yellow-soft))}
  .what-body{position:absolute;top:86px;left:0;right:0;padding:0 12px 0 16px}
  .what-body .sub{font-family:"Barlow Condensed",sans-serif;font-weight:600;font-size:11.5px;line-height:1.15;color:var(--yellow-deep);margin-bottom:5px}
  .what-body .body{font-size:9.2px;line-height:1.38}
  .what-body .body p{margin-bottom:8px}
  .what-list{list-style:none}
  .what-list li{position:relative;padding-left:9px;font-size:9.2px;line-height:1.35;margin-bottom:6px}
  .what-list li::before{content:"";position:absolute;left:0;top:3px;width:5px;height:5px;background:var(--yellow)}
</style>
</head>
<body>

<!-- Outside of the brochure -->
<section class="spread spread--outside">
  <article class="panel dealers">
    <div class="photo-fade" role="img" aria-label="Faded photo of a car in a dealership showroom"></div>
    <h2 class="heading">Automobile Dealerships</h2>
    <p class="lead">We can install a secure wireless system that covers the entire dealership and lots.</p>
    <ul class="bullets">
      <li>We can install a system that enables your sales representatives to be much more productive and successful.</li>
      <li>We equip tablets to access your database of inventory and then present the data through our presentation app.</li>
    </ul>
    <div class="body">
      <p>Today your sales representatives might be carrying sheets of paper as they walk through the sales lot with prospective customers and then fumble through them to obtain limited information about the model that the customer expresses an interest in. Instead, your sales representatives can now walk with a tablet; no paper based system or relying on memory. Instantly they can access data about every model. Proprietary information can be displayed about the car. These items might be minimum sales price, desired sales price, the specific sales representative daily or monthly goals (and current numbers).</p>
      <p>Another possibility would be the display of potential sales incentives or bonuses the sales representative could earn on this model. The sales representative could also instantly access pertinent information about that particular model and associated options. This instantly allows the sales representative to push particulars that the customer might already have expressed an interest in (horsepower, mpg, type of drivetrain, etc.).</p>
      <p>There could be notes that the sales manager had entered about specific cars being pushed that day. The sales representative could instantly text the sales manager with specifics if the customer was close to purchasing instead of saying “Let’s go back to my office and let me check with my manager”, thereby greatly expediting the entire sales process and more likely closing the deal by eliminating those moments of hesitation or loss of enthusiasm by the customer.</p>
    </div>
  </article>

  <article class="panel">
    <div class="projects-top">
      <h2 class="heading">Some Recent Projects</h2>
      <ul class="bullets">
        <li>Resolved a major problem at SRU for one of their computer clusters used in their research department.</li>
        <li>Participated in a twenty million dollar project for the State of RI to upgrade all school environments to provide connectivity for every student on high speed wireless (1:1 computing).</li>
        <li>Created an open-source implementation in a large commercial environment. Designed an open-source mail server running on the public cloud for hundreds of users.</li>
        <li>Provided 24x7 monitoring and support for a large boarding school. Designed and installed a wireless LAN that covered a large campus and also integrated a security camera system. Created a mobile device management system for student tablets, providing appropriate student permissions.</li>
        <li>Created a directory domain and related security for a newly constructed medical office. Connected an ultrasound machine to the IT network and enabled external authorized doctors to securely connect to the server to view ultrasound recordings.</li>
      </ul>
    </div>
    <div class="solutions">
      <p class="solutions-text">Our solutions for schools, medical/dental, small businesses and auto dealerships are cost effective because they are customized specifically for your environment. Your type of business and end users are critical factors that should be the influencing design parameters</p>
      <ul class="contact">
        <li><svg viewBox="0 0 10 10"><circle cx="5" cy="5" r="5" fill="#fff"/><rect x="2.5" y="3" width="5" height="3.2" fill="none" stroke="#1788a6" stroke-width=".8"/><line x1="4" y1="7.4" x2="6" y2="7.4" stroke="#1788a6" stroke-width=".8"/></svg>www.keystonenet-it.com</li>
        <li><svg viewBox="0 0 10 10"><circle cx="5" cy="5" r="5" fill="#fff"/><rect x="2.4" y="3.2" width="5.2" height="3.6" fill="none" stroke="#1788a6" stroke-width=".8"/><polyline points="2.4,3.2 5,5.3 7.6,3.2" fill="none" stroke="#1788a6" stroke-width=".8"/></svg>hello@keystonenet-it.com</li>
        <li><svg viewBox="0 0 10 10"><circle cx="5" cy="5" r="5" fill="#fff"/><path d="M3.3 2.6 L4.4 2.6 L4.9 4 L4.2 4.6 Q4.8 5.8 5.9 6.3 L6.5 5.6 L7.8 6.2 L7.8 7.3 Q5.6 7.6 4 6 Q2.6 4.5 3.3 2.6 Z" fill="#1788a6"/></svg>401-555-0148</li>
        <li><svg viewBox="0 0 10 10"><circle cx="5" cy="5" r="5" fill="#fff"/><path d="M5 8.2 Q2.8 5.6 2.8 4.2 A2.2 2.2 0 0 1 7.2 4.2 Q7.2 5.6 5 8.2 Z" fill="#1788a6"/><circle cx="5" cy="4.2" r=".8" fill="#fff"/></svg>18 Elm St #210 Harborview, RI 02900-0210</li>
      </ul>
    </div>
  </article>

  <article class="panel cover">
    <div class="cover-photo" role="img" aria-label="Photo of two smiling professionals reviewing a tablet together"></div>
    <div class="brand"><span class="brand-dot"></span>Keystone Net</div>
    <div class="cover-band">
      <h1 class="cover-title">We Do<br>Everything</h1>
      <p class="cover-sub"><b>Design, Install, Modify</b><br><span>and</span> <b>Monitor(24x7)</b></p>
      <div class="cover-for">
        <span class="for">for</span>
        <div>
          <div class="cover-item">
            <h3>IT Environments</h3>
            <p>Each environment is customized for either schools, medical/ dental, small businesses or auto dealerships</p>
          </div>
          <div class="cover-item">
            <h3>Security Camera<br>Monitoring Systems</h3>
            <p>HD, digital and economically integrated into the IT environment</p>
          </div>
        </div>
      </div>
    </div>
  </article>
</section>

<!-- Inside of the brochure -->
<section class="spread spread--inside">
  <div class="panel" style="width:500px">
    <div class="inside-band band-teal"></div>
    <h2 class="why-title">Why Outsource?</h2>
    <div class="inside-photo" role="img" aria-label="Photo of a happy customer holding up a new car key"></div>
    <div class="why-col why-col--a">
      <p class="lead">We specialize in IT support at a scale tailored to your exact requirements</p>
      <div class="body">
        <p>A direct, dedicated IT staff will have either idle time during periods of stability or inadequate resources for those times when problems occur simultaneously.</p>
        <p>By outsourcing to Keystone Net your business will always have the ideal level of support, and therefore never overpay nor be insufficiently prepared to deal with sudden problems that can overwhelm insufficient numbers of staff.</p>
        <p>Because funds are allocated efficiently your business can now afford to capitalize on the most current technology and benefit from all features offered by these newest features.</p>
      </div>
    </div>
    <div class="why-col why-col--b">
      <div class="body">
        <p>Outsourcing is the better economical choice; there are no overtime hours, paid vacations, morale problems, costs associated with health care and mandatory reporting, and other overhead expenses associated with employees.</p>
        <p>But cost is not the only reason to outsource. Your core business is not IT; therefore outsourcing eliminates the need for your personnel to be proficient in multiple areas, i.e. building specialized skills to support your core businesses and functions as well as accumulating skills enabling them to manage, enhance and maintain the ideal IT environment.</p>
        <p>The elimination of this responsibility allows you to focus on finding and developing personnel skills directly related to your business, and not compromising your core business components.</p>
      </div>
    </div>
  </div>

  <article class="panel what-panel">
    <div class="inside-band band-yellow"></div>
    <h2 class="what-title">What we do<br>for all types of IT<br>environments</h2>
    <div class="what-body">
      <p class="sub">Install, customize and support all elements of IT environments</p>
      <div class="body"><p>We analyze your unique business requirements, determining if modifications are cost justified for your existing computing environment.</p></div>
      <p class="sub">Design the best combination of hardware and software for your environment</p>
      <div class="body"><p>We specialize in leading desktop, network, server and mobile platforms, tablets and smart phones. We are able to structure each solution to the specific type of business to achieve the best returns on investment.</p></div>
      <p class="sub">Tailor all components of the entire IT environment</p>
      <div class="body"><p>Install, customize, monitor</p></div>
      <ul class="what-list">
        <li>desktops</li>
        <li>multiple operating systems (desktop, mobile, server, embedded)</li>
        <li>tablets</li>
        <li>network backbones and their components (Ethernet, fiber, routers, switches, advanced wireless)</li>
        <li>servers</li>
        <li>virtualization (thin clients/zero clients)</li>
        <li>firewalls</li>
        <li>virus/intruder detection</li>
        <li>data encryption</li>
        <li>data analysis and more</li>
      </ul>
    </div>
  </article>
</section>

</body>
</html>
```